Willowmere Paws Gala Sponsor & Stallholder Leaflet Design

Willowmere Paws Gala is the updated and refreshed version of the Brackenfield Pup Fair (See www.brackenfieldpupfair.co.uk).
Under new management, we need a leaflet designed to promote the event to potential stallholders and sponsors.
Willowmere Paws Gala is a fun day out for dogs and their human companions, with a range of activities for both.
As this is an outdoor event, we would like this theme in the leaflet.
It is being held in the grounds of Ashcombe Hall - http://www.ashcombehall.com
Attached is the required copy.
Note:
Leaflet format of DL/6 page is preferred, but will accept A5/4page
I will require the final work in InDesign format
Target Market(s)
Dog owners and lovers
Industry/Entity Type
Event
Look and feel

```html
<!DOCTYPE html>
<html lang="en">
<head>
<meta charset="utf-8">
<title>Willowmere Paws Gala – Sponsor &amp; Stallholder Leaflet</title>
<link rel="stylesheet" href="https://fonts.googleapis.com/css2?family=Fredoka:wght@600;700&family=Raleway:wght@400;600;700&family=Oswald:wght@500&family=Arimo:wght@400;700&display=swap">
<style>
:root{
  --paper:#ffffff;
  --ink:#222222;
  --forest:#1f5a1d;
  --leaf:#5a9a3a;
  --panel:#629f48;
  --rule:#2c6a26;
  --band:#2d5e22;
  --band-text:#b6d98a;
  --sun:#f6c500;
  --white:#ffffff;
}
*{margin:0;padding:0;box-sizing:border-box}
html,body{width:1200px;height:843px;overflow:hidden;background:var(--paper)}
.leaflet{position:relative;width:1200px;height:843px;overflow:hidden;font-family:"Raleway",sans-serif;color:var(--ink)}

/* left panel */
.intro{position:absolute;left:0;top:0;width:391px;height:843px;background:var(--paper)}
.copy{position:absolute;left:31px;width:337px;font-size:11.3px;line-height:14.6px;text-align:justify}
.copy .lead{font-size:14px}
.heading{position:absolute;font-family:"Fredoka",sans-serif;font-weight:700;font-size:27px;line-height:27px;letter-spacing:.3px}
.heading.dark{color:var(--forest)}
.heading.light{color:var(--leaf)}
.promo-list{position:absolute;left:38px;top:684px;width:240px;list-style:none;font-weight:700;font-size:12.4px;line-height:20px}
.promo-list li{position:relative;padding-left:18px;white-space:nowrap}
.promo-list li::before{content:"";position:absolute;left:0;top:6px;width:9px;height:9px;background:var(--leaf)}
.puppy{position:absolute;left:290px;top:676px;width:68px;height:124px;border-radius:34px 34px 18px 18px;background:radial-gradient(ellipse at 50% 40%,#7a4a2a,#4a2a16 70%,transparent 72%)}

/* middle panel */
.form-panel{position:absolute;left:391px;top:0;width:370px;height:843px;background:var(--panel);font-family:"Arimo",sans-serif;color:var(--forest)}
.form-title{position:absolute;left:0;top:17px;width:100%;text-align:center;color:var(--white);font-weight:700;font-size:14.5px}
table{border-collapse:collapse;position:absolute}
td{border:1.5px solid var(--rule);padding:0 4px;white-space:nowrap;vertical-align:middle}
.contact{left:36px;top:47px;width:316px}
.contact td{height:29.6px;font-weight:700;font-size:12px}
.contact td:first-child{width:134px}
.grid{font-size:7.6px}
.grid td{height:16px}
.note{position:absolute;font-size:7.6px}
.outside{left:36px;top:266px;width:300px}
.inside{left:36px;top:364px;width:300px}
.guide{left:36px;top:454px;width:271px}
.banners{left:36px;top:578px;width:214px}
.totals{left:36px;top:620px;width:272px}
.terms{position:absolute;left:0;top:697px;width:370px;height:146px;background:var(--band);padding:12px 24px 0 26px;color:var(--band-text);font-weight:700;font-size:9.2px;line-height:11.2px;text-align:justify}

/* cover */
.cover{position:absolute;left:761px;top:0;width:439px;height:843px}
.photo{position:absolute;inset:0;background:linear-gradient(180deg,#3c6a2a 0%,#4f8435 25%,#6aa84a 45%,#5c9a3c 70%,#467e2c 100%)}
.title{position:absolute;left:0;width:100%;text-align:center;font-family:"Fredoka",sans-serif;font-weight:700;line-height:1}
.title.top{top:130px;font-size:42px;color:var(--sun)}
.title.bottom{top:178px;font-size:48px;color:var(--white)}
.dates{position:absolute;left:0;top:245px;width:100%;text-align:center;font-family:"Oswald",sans-serif;font-weight:500;font-size:18px;color:var(--white);letter-spacing:.5px}
.cover-band{position:absolute;left:0;bottom:0;width:100%;height:100px}
.cover-band svg{position:absolute;left:0;top:0}
.cover-band p{position:absolute;left:0;bottom:12px;width:100%;text-align:center;font-family:"Oswald",sans-serif;font-weight:500;font-size:16px;color:var(--band-text);letter-spacing:.4px}
</style>
</head>
<body>
<main class="leaflet">

  <section class="intro">
    <p class="copy" style="top:34px"><span class="lead">Brackenfield Pup Fair</span> was created and launched in 2009, in aid of Homefront Helpers, co-inciding with the deployment of the Border Lancers on active service to Afghanistan. Parents left behind during their deployment where amongst the committed volunteers who participated and helped in the organisation of the event. The event captured the animal loving spirit of Norfolk at a point when the whole county was passionate in their support of 'our blokes doing their bit' in Afghanistan. Expecting a few hundred dogs and 5,000 humans, it actual attracted circa 1,000 dogs, with almost 15,000 guests, the inaugural event was seen as an outstanding success. 2010 saw a visitor increase of circa 20%.</p>
    <p class="copy" style="top:226px">Due to the overwhelming footfall, 2013 will become a two day event and is now known as 'Willowmere Paws Gala'.</p>

    <h2 class="heading dark" style="left:57px;top:268px">Where Is It Held?</h2>
    <p class="copy" style="top:315px">Ashcombe Hall is one of Norfolk's most romantic and impressive large Edwardian country houses set in sweeping parkland. It was built to a grand design by Edmund Albert Hale, grandson of Edmund Hale, the inventor of modern holiday travel, and is lived in today by his descendants. Although a private family home, and not open to the public, Ashcombe Hall offers a unique and magical venue for the Brackenfield Pup Fair.</p>
    <p class="copy" style="top:446px">Near Fakenham, in North Norfolk, Ashcombe Hall is approximately 30 minutes from Norwich.</p>

    <h2 class="heading light" style="left:57px;top:494px">Who Will Attend?</h2>
    <p class="copy" style="top:533px">The target audience for this event is anyone who likes, owns or has an interest in dogs! Heavily promoted to dog lovers and owners, across several mediums, it attracts visitors of all ages across the demographic spectrum.</p>

    <h2 class="heading light" style="left:54px;top:610px">How Will It</h2>
    <h2 class="heading light" style="left:36px;top:636px">Be Promoted?</h2>
    <ul class="promo-list">
      <li>Dedicated website</li>
      <li>Social Media - Pawbook, Chirper etc</li>
      <li>Regional Advertising</li>
      <li>Dog &amp; pet Press</li>
      <li>Regional Radio</li>
      <li>Regional database via email</li>
    </ul>
    <div class="puppy" role="img" aria-label="Photo of a brown dachshund puppy sitting"></div>
  </section>

  <section class="form-panel">
    <h1 class="form-title">Exhibitor Space Application Form</h1>
    <table class="contact">
      <tr><td>Business Name</td><td></td></tr>
      <tr><td>Business Address</td><td></td></tr>
      <tr><td>Postcode</td><td></td></tr>
      <tr><td>Business Website</td><td></td></tr>
      <tr><td>Contact Name</td><td></td></tr>
      <tr><td>Contact Email</td><td></td></tr>
    </table>

    <p class="note" style="left:36px;top:241px">Space Required</p>
    <p class="note" style="left:224px;top:239px">Note - All Prices Exclude VAT</p>
    <p class="note" style="left:36px;top:253px">Outside</p>
    <table class="grid outside">
      <tr><td style="width:113px">Space</td><td style="width:64px">Price</td><td style="width:66px"></td><td>Total</td></tr>
      <tr><td>3m(w) x 6m(d)</td><td>&nbsp;&nbsp;@ £150</td><td></td><td></td></tr>
      <tr><td>6m(w) x 10m(d)</td><td>&nbsp;&nbsp;@ £250</td><td></td><td></td></tr>
      <tr><td>9m(w) x 10m(d)</td><td>&nbsp;&nbsp;@ £350</td><td></td><td></td></tr>
      <tr><td>12m(w) x 10m(d)</td><td>&nbsp;&nbsp;@ £450</td><td></td><td></td></tr>
    </table>

    <p class="note" style="left:36px;top:352px">Inside</p>
    <table class="grid inside">
      <tr><td style="width:113px">Space</td><td style="width:64px">Price</td><td style="width:64px">&nbsp;&nbsp;Quantity</td><td>&nbsp;&nbsp;Total</td></tr>
      <tr><td>Marquee Space&nbsp; Min 6m2</td><td>@ £15/m2</td><td></td><td></td></tr>
      <tr><td>Power&nbsp;&nbsp; Per 13amp Socket</td><td>@ £30 each</td><td></td><td></td></tr>
      <tr><td>Table (6' x 2'6")</td><td>@ £10 each</td><td></td><td></td></tr>
    </table>

    <p class="note" style="left:40px;top:443px">Show Guide Advert</p>
    <table class="grid guide">
      <tr><td style="width:113px">Space - mm's</td><td style="width:50px">Price</td><td style="width:48px">Quantity</td><td>Total</td></tr>
      <tr><td>Back cover - 148w x210h</td><td>£350</td><td></td><td></td></tr>
      <tr><td>Full page - 148w x 210h</td><td>£250</td><td></td><td></td></tr>
      <tr><td>Half Page - 148w x 105h</td><td>£135</td><td></td><td></td></tr>
      <tr><td>Quarter Page&nbsp; - 74w x 105h</td><td>£75</td><td></td><td></td></tr>
      <tr><td>Sixth Page&nbsp; -&nbsp; 74w x 70h</td><td>£50</td><td></td><td></td></tr>
      <tr><td>Voucher Booklet</td><td>£50</td><td></td><td></td></tr>
    </table>

    <table class="grid banners">
      <tr><td style="width:113px">Banners (60cm high)</td><td style="width:62px">@ £10 per mtr</td><td></td></tr>
    </table>
    <p class="note" style="left:36px;top:601px">In Competition Rings - design &amp; print not included</p>

    <table class="grid totals">
      <tr><td style="width:198px;height:12.5px">Sub Total</td><td style="height:12.5px"></td></tr>
      <tr><td style="height:12.5px">VAT @ 20%</td><td style="height:12.5px"></td></tr>
      <tr><td style="height:12.5px">Grand Total</td><td style="height:12.5px"></td></tr>
      <tr><td style="height:12.5px">Deposit</td><td style="height:12.5px;text-align:center">£50</td></tr>
      <tr><td style="height:12.5px">Outstanding</td><td style="height:12.5px"></td></tr>
    </table>

    <div class="terms">
      <p>To secure the booking this form must be fully completed and signed AND accompanied by the deposit and a post dated cheque (made payable to Harrow Lane Events Ltd) for the outstanding balance dated one month prior to the show. If you are paying by debit/credit card, we will call you to take the deposit payment.Bookings are subject to terms &amp; conditions and booking the event confirms that you accept these conditions.</p>
      <p>PLEASE RETURN COMPLETED FORM TO - Willowmere Paws Gala, Harrow Lane Events Ltd, 7 Fernbrook Lane, Little Hadley, Holt NR99 1ZZ</p>
    </div>
  </section>

  <section class="cover">
    <div class="photo" role="img" aria-label="Photo of a young woman sitting on a sunny lawn hugging a pale labrador, with trees blurred behind"></div>
    <h1 class="title top">Willowmere</h1>
    <h1 class="title bottom">Paws Gala</h1>
    <p class="dates">27TH &nbsp;&amp;&nbsp; 28TH &nbsp;JULY 2013</p>
    <div class="cover-band">
      <svg width="439" height="100" viewBox="0 0 439 100" aria-hidden="true">
        <defs>
          <linearGradient id="bandFade" x1="0" y1="0" x2="0" y2="1">
            <stop offset="0" stop-color="#2d5e22" stop-opacity="0"/>
            <stop offset=".55" stop-color="#2d5e22" stop-opacity=".85"/>
            <stop offset="1" stop-color="#244d1b"/>
          </linearGradient>
        </defs>
        <polygon points="0,30 180,50 439,20 439,100 0,100" fill="url(#bandFade)"/>
      </svg>
      <p>SPONSORSHIP &amp; TRADE EXHIBITOR OPPORTUNITIES</p>
    </div>
  </section>

</main>
</body>
</html>
```